Bright Lantern Media Works Brochure

We need a DOUBLE GATE FOLD 4 PANEL brochure for our video production company. The brochure will show pics of our green screen studio, some post production images "like the weatherman" standing in front of a weather map, and descriptions of our services and pricing. I really want this to look professional and classy. I will upload photos I want to use.
Updates

Reason: Never mind. I cannot extend it 5 days. Just refund my money since no one has submitted a design.

Reason: We need a better design than what we have gotten. Half the submissions didn't even give us a gate fold as instructed.

Target Market(s)

The main target of our company is physicians and other medical professionals. More men than women.

Industry/Entity Type

It Company

Font styles to use
Serif
Sans Serif

Requirements
Must have
• Professional, high end.
Colors - the logo is on black. I would try to make the brochure black so the colors and images pop off the page. Our colors are blue and white as in the logo.
Nice to have
• It should be able to be mailed so the ouside back should be white with a place for a label to be attached.

```html
<!DOCTYPE html>
<html lang="en">
<head>
<meta charset="utf-8">
<title>Bright Lantern Media Works Brochure</title>
<link href="https://fonts.googleapis.com/css2?family=Open+Sans:ital,wght@0,400;0,600;1,400;1,600&display=swap" rel="stylesheet">
<style>
  :root {
    --bg: #e4e4e4;
    --ink: #0b0b0b;
    --brand-blue: #1f9ed6;
    --deep-blue: #137fb6;
    --sky: #3fb6ea;
    --text-light: #ffffff;
    --fold: rgba(255,255,255,0.18);
  }
  * { box-sizing: border-box; margin: 0; padding: 0; }
  html, body { width: 1200px; height: 895px; overflow: hidden; }
  body {
    background: var(--bg);
    font-family: "Open Sans", Arial, sans-serif;
    position: relative;
    color: var(--text-light);
  }

  /* ---------- inside spread ---------- */
  .inside-spread {
    position: absolute; left: 30px; top: 18px;
    width: 1140px; height: 420px;
    display: flex;
    box-shadow: 0 6px 18px rgba(0,0,0,0.25);
  }
  .panel-about {
    width: 570px; height: 100%;
    background: var(--ink);
    position: relative;
  }
  .panel-about .about-top { padding: 16px 22px 0; height: 130px; }
  .section-title {
    font-weight: 400; color: var(--sky);
    font-size: 20px; line-height: 1.2; margin-bottom: 6px;
  }
  .body-copy { font-size: 9.5px; line-height: 1.35; color: var(--text-light); }
  .body-copy.accent { color: var(--sky); font-style: italic; margin-top: 6px; }
  .studio-photo {
    height: 122px;
    background: linear-gradient(90deg, #7bc24a 0%, #9fd15b 35%, #3a3a3a 60%, #1a1a1a 100%);
  }
  .panel-about .about-bottom { padding: 16px 22px 0; }
  .panel-about .about-bottom .body-copy { columns: 2; column-gap: 20px; }

  .panel-services {
    width: 285px; height: 100%;
    background: var(--brand-blue);
    padding: 14px 16px;
    position: relative;
  }
  .panel-services + .panel-services { border-left: 1px solid var(--fold); }
  .panel-services .section-title { color: var(--text-light); font-size: 18px; }
  .panel-services .body-copy { font-size: 8.5px; }
  .service { margin-top: 12px; }
  .service-name {
    display: flex; align-items: center; gap: 8px;
    font-size: 13px; font-weight: 600; margin-bottom: 6px;
  }
  .service-mark { width: 12px; height: 12px; border-radius: 50%; background: var(--text-light); }
  .service-image { height: 64px; margin-bottom: 6px; }
  .img-corporate { background: linear-gradient(135deg, #e9f1f7, #9fc3dd); }
  .img-commercial { background: linear-gradient(180deg, #7fb6e6 0%, #b7d6ee 55%, #3d7a3a 100%); }
  .img-animated { background: linear-gradient(180deg, #fbfbf5 0%, #f3d7b8 50%, #5aaad6 100%); }
  .divider { height: 1px; background: rgba(255,255,255,0.5); margin: 12px 0 0; }

  /* ---------- cover ---------- */
  .cover {
    position: absolute; left: 315px; top: 458px;
    width: 570px; height: 420px;
    overflow: hidden;
    box-shadow: 0 6px 18px rgba(0,0,0,0.3);
    background: var(--brand-blue);
  }
  .cover-art { position: absolute; inset: 0; }
  .cover-fold {
    position: absolute; left: 285px; top: 0; bottom: 0;
    width: 1px; background: var(--fold);
  }
  .brand {
    position: absolute; left: 14px; top: 84px; width: 262px;
    display: flex; align-items: center; gap: 8px;
    font-size: 16px; font-weight: 400; color: var(--sky);
    white-space: nowrap;
  }
  .brand-dot { width: 12px; height: 12px; border-radius: 50%; background: var(--sky); flex: none; }
  .tagline {
    position: absolute; left: 285px; width: 285px; top: 20px;
    text-align: center; font-style: italic; line-height: 1.25;
  }
  .tagline .small { font-size: 14px; display: block; }
  .tagline .large { font-size: 21px; color: var(--sky); display: block; }
  .filmstrip-photo {
    position: absolute; left: 30px; top: 192px;
    width: 520px; height: 128px;
    background: linear-gradient(90deg, #1d3550 0%, #2b4a72 50%, #1a2a44 100%);
  }
  .call-out { position: absolute; left: 36px; top: 332px; }
  .call-out .label { font-size: 16px; font-weight: 600; }
  .call-out .phone { font-size: 24px; font-weight: 600; margin-top: 2px; }
</style>
</head>
<body>

<section class="inside-spread">
  <div class="panel-about">
    <div class="about-top">
      <h2 class="section-title">Who we are?</h2>
      <p class="body-copy">Lorem ipsum dolor sit amet, consectetuer adipiscing elit, sed diam nonummy nibh euismod tincidunt ut laoreet dolore magna aliquam erat volutpat. Ut wisi enim ad minim veniam, quis nostrud exerci tation ullamcorper suscipit lobortis nisl ut aliquip ex ea commodo consequat.</p>
      <p class="body-copy accent">Duis autem vel eum iriure dolor in hendrerit in vulputate velit esse molestie consequat, vel illum dolore eu feugiat nulla facilisis at vero eros et accumsan et iusto odio dignissim nulla.</p>
    </div>
    <div class="studio-photo" role="img" aria-label="Green screen studio with a video camera in the foreground"></div>
    <div class="about-bottom">
      <h2 class="section-title">Why we are different</h2>
      <p class="body-copy">Lorem ipsum dolor sit amet, consectetuer adipiscing elit, sed diam nonummy nibh euismod tincidunt ut laoreet dolore magna aliquam erat volutpat. Ut wisi enim ad minim veniam, quis nostrud exerci tation ullamcorper suscipit lobortis nisl ut aliquip ex ea commodo consequat. Duis autem vel eum iriure dolor in hendrerit in vulputate velit esse molestie consequat, vel illum dolore eu feugiat nulla facilisis.</p>
    </div>
  </div>

  <div class="panel-services">
    <h2 class="section-title">What we do?</h2>
    <p class="body-copy">Lorem ipsum dolor sit amet, consectetuer adipiscing elit, sed diam nonummy nibh euismod tincidunt ut laoreet dolore magna aliquam erat volutpat. Ut wisi enim ad minim veniam, quis nostrud exerci tation ullamcorper suscipit lobortis nulla facilisi.</p>
    <div class="service">
      <h3 class="service-name"><span class="service-mark"></span>Corporate Video</h3>
      <div class="service-image img-corporate" role="img" aria-label="Hand touching a screen of medical interface icons"></div>
      <p class="body-copy">Lorem ipsum dolor sit amet, consectetuer adipiscing elit, sed diam nonummy nibh euismod tincidunt ut laoreet dolore magna aliquam erat volutpat. Duis dolore te feugait nulla facilisi.</p>
    </div>
  </div>

  <div class="panel-services">
    <div class="service">
      <h3 class="service-name"><span class="service-mark"></span>Commercial Video</h3>
      <div class="service-image img-commercial" role="img" aria-label="Runner jogging outdoors under a blue sky"></div>
      <p class="body-copy">Lorem ipsum dolor sit amet, consectetuer adipiscing elit, sed diam nonummy nibh euismod tincidunt ut laoreet dolore magna aliquam erat volutpat. Duis dolore te feugait nulla facilisi.</p>
    </div>
    <div class="divider"></div>
    <div class="service">
      <h3 class="service-name"><span class="service-mark"></span>Animated Video</h3>
      <div class="service-image img-animated" role="img" aria-label="Flat illustrated city skyline"></div>
      <p class="body-copy">Lorem ipsum dolor sit amet, consectetuer adipiscing elit, sed diam nonummy nibh euismod tincidunt ut laoreet dolore magna aliquam erat volutpat. Duis dolore te feugait nulla facilisi.</p>
    </div>
  </div>
</section>

<section class="cover">
  <svg class="cover-art" width="570" height="420" viewBox="0 0 570 420" aria-hidden="true">
    <defs>
      <linearGradient id="coverBlue" x1="0" y1="0" x2="1" y2="1">
        <stop offset="0" stop-color="#0f6ea3"/>
        <stop offset="0.5" stop-color="#1f9ed6"/>
        <stop offset="1" stop-color="#3fb6ea"/>
      </linearGradient>
    </defs>
    <rect width="570" height="420" fill="url(#coverBlue)"/>
    <polygon points="0,0 570,0 570,140 0,178" fill="#0b0b0b"/>
    <polygon points="0,178 570,140 570,146 0,184" fill="#3fb6ea"/>
  </svg>
  <div class="filmstrip-photo" role="img" aria-label="Film strip of night city and travel photographs"></div>
  <div class="cover-fold"></div>

  <div class="brand"><span class="brand-dot"></span>Bright Lantern Media Works</div>
  <div class="tagline">
    <span class="small">Make your</span>
    <span class="large">videos stand out</span>
    <span class="small">from the crowd</span>
  </div>
  <div class="call-out">
    <p class="label">Call Us Today</p>
    <p class="phone">123 456 7890</p>
  </div>
</section>

</body>
</html>
```